Drapery & Decor Atelier Project…
I am looking for a new website design for a store front “Drapery & Decor Atelier” business. Their customer would walk in off the street to have curtains designed for their home or business. This is not an ecommerce website.
The website colors should be light blue, dark blue, white and maybe tan. Be creative.
The curtains they sell can be found at www.plvexo.example and www.dombly.example. Please use images from these two website.
Navigation:
Home
Our Studio
Our Services
Our Manufactures
PLVEXO
Dombly
Our Process
Testimonials
Refer a Client
Subscribe to our Newsletter
Our Blog – (Needed for Internet Marketing)
Contact Us
The website should have a large footer for internet marketing purposes.
Updates
Great designs. Thank you everyone. I have sent them all to the client and i am waiting for feedback. I will let everyone know as soon as possible.
Sorry for the delay everyone. The client has been on vacation and has not provided feedback yet. As soon as I have an update I will let everyone know.

```html
<!DOCTYPE html>
<html lang="en">
<head>
<meta charset="utf-8">
<title>Drapery &amp; Decor Atelier</title>
<link rel="stylesheet" href="https://fonts.googleapis.com/css2?family=Open+Sans:wght@400;600&family=Yanone+Kaffeesatz:wght@400&display=swap">
<style>
:root{
  --royal:#1638c4;
  --royal-deep:#08208f;
  --royal-light:#2f5ae0;
  --sky:#a4c1f7;
  --sky-soft:#a9c0ec;
  --navy:#0d2470;
  --nav-text:#2d3c66;
  --text:#333333;
  --panel:#efefef;
  --panel-line:#c6c6c6;
  --white:#ffffff;
}
*{margin:0;padding:0;box-sizing:border-box}
html,body{width:1016px;height:1200px;overflow:hidden;background:var(--white)}
body{position:relative;font-family:"Open Sans",Arial,sans-serif;color:var(--text)}
.backdrop{position:absolute;left:0;width:1016px;
  background:linear-gradient(90deg,var(--royal-deep) 0%,var(--royal) 30%,var(--royal-light) 50%,var(--royal) 70%,var(--royal-deep) 100%)}
.backdrop-top{top:0;height:384px}
.backdrop-bottom{top:1149px;height:51px}
.sky-band{position:absolute;left:0;top:384px;width:1016px;height:136px;background:var(--sky)}
.header-panel{position:absolute;left:36px;top:67px;width:940px;height:453px;background:var(--sky)}
.utility{position:absolute;top:21px;left:552px;display:flex;align-items:center;font-size:12.5px}
.btn{height:28px;padding:0 17px;line-height:27px;background:linear-gradient(#ffffff,#dfe7fa);border:1px solid #9fb2e0;border-radius:3px;color:var(--royal-deep);margin-right:5px}
.utility .links{margin-left:11px;color:#d6e1ff;font-size:12px}
.utility .links span{margin:0 5px;color:#8ea6ef}
.brand{position:absolute;left:48px;top:82px;font-family:"Yanone Kaffeesatz",sans-serif;font-size:29px;color:#5d6d8e;letter-spacing:.3px}
.main-nav{position:absolute;top:85px;left:279px;height:30px;font-size:13.5px;color:var(--nav-text)}
.main-nav a{position:absolute;top:0;line-height:29px;white-space:nowrap;text-decoration:none;color:inherit}
.main-nav .current{left:0;width:66px;height:30px;text-align:center;background:linear-gradient(#ffffff,#d9e1f1);border:1px solid #b2bfd8;border-radius:2px;color:var(--royal)}
.hero{position:absolute;left:45px;top:132px;width:921px;height:333px;
  background:linear-gradient(90deg,#d9d5ce 0%,#e7e8ea 25%,#f3f0e8 45%,#dcdfe3 60%,#f0ece2 78%,#d6d9dd 100%)}
.hero-shadow{position:absolute;left:65px;top:461px;width:880px;height:30px;border-radius:50%;background:radial-gradient(ellipse at center,rgba(60,80,140,.45) 0%,rgba(60,80,140,0) 70%)}
.dots{position:absolute;top:495px;left:474px;display:flex;gap:6px}
.dots i{width:13px;height:13px;border-radius:50%;background:radial-gradient(circle at 40% 35%,#fff,#cbd6ee);border:1px solid #8ea0c8}
.dots i.on{background:radial-gradient(circle at 40% 35%,#8195c4,#3d4f86)}
h1,h2{font-weight:400;color:var(--navy)}
.welcome{position:absolute;left:43px;top:544px;width:600px}
.welcome h1{font-size:30px;line-height:40px}
.welcome p{font-size:12px;line-height:17.3px;color:#333;margin-left:3px}
.read-more{position:absolute;font-size:12px;color:var(--sky-soft)}
.products-title{position:absolute;left:48px;top:729px;font-size:23px}
.product{position:absolute;width:141px;height:148px;overflow:hidden}
.product .tint{position:absolute;inset:0}
.product .more{position:absolute;left:0;bottom:0;width:100%;height:26px;background:rgba(255,255,255,.55);font-size:13px;color:#222;text-align:right;padding-right:26px;line-height:26px}
.product .more svg{position:absolute;right:5px;top:5px}
.tone-fringe{background:radial-gradient(circle at 30% 35%,#c9c98a,#8a8a55 55%,#5e5a3c)}
.tone-damask{background:linear-gradient(135deg,#c9ad95,#e0cbb6 50%,#b59479)}
.tone-ikat{background:linear-gradient(135deg,#bdbba5,#8f9c9e 50%,#6e6a55)}
.tone-swatch{background:linear-gradient(135deg,#3e2a26,#6d8aa6 45%,#a7b8c6 60%,#2a1d1b)}
.side-box{position:absolute;left:657px;width:317px;background:var(--panel);border:1px solid var(--panel-line)}
.side-box h2{font-size:23px;margin:14px 24px 0;line-height:30px;border-bottom:1px solid #b9b9b9;width:290px}
.testimonials{top:544px;height:287px}
.quote{margin:10px 0 0 26px;width:270px;font-size:12.3px;line-height:16px;color:#333;padding-bottom:7px;border-bottom:1px dashed #999}
.quote+.quote{margin-top:8px}
.services{top:848px;height:238px}
.service-list{list-style:none;margin:20px 0 0 26px;font-size:12.8px;color:#333}
.service-list li{line-height:24px;padding-left:16px;position:relative}
.service-list li::before{content:"";position:absolute;left:0;top:8px;width:9px;height:9px;border-radius:50%;background:radial-gradient(circle at 40% 35%,#8ea2cf,#3d4f86)}
.site-footer{position:absolute;left:35px;top:1114px;width:940px;height:55px;background:var(--sky);text-align:center;font-size:10.5px;line-height:55px;color:#4c5a80}
</style>
</head>
<body>
<div class="backdrop backdrop-top" role="img" aria-label="Deep blue stage curtain backdrop"></div>
<div class="sky-band"></div>
<div class="backdrop backdrop-bottom" role="img" aria-label="Deep blue stage curtain backdrop"></div>

<nav class="utility">
  <span class="btn">Refer a Client</span>
  <span class="btn">Subscribe to our Newsletter</span>
  <span class="links">Blog<span>|</span>Contact Us</span>
</nav>

<header class="header-panel"></header>
<div class="brand">Drapery &amp; Decor Atelier</div>
<nav class="main-nav">
  <a class="current">Home</a>
  <a style="left:79px">Studio</a>
  <a style="left:146px">Services</a>
  <a style="left:224px">Manufactures</a>
  <a style="left:335px">PLVEXO</a>
  <a style="left:420px">Dombly</a>
  <a style="left:486px">Our Process</a>
  <a style="left:586px">Testimonials</a>
</nav>

<div class="hero" role="img" aria-label="Bright room with tied-back cream curtains framing tall windows between white brick pillars"></div>
<div class="hero-shadow"></div>
<div class="dots"><i></i><i></i><i class="on"></i></div>

<section class="welcome">
  <h1>Welcome!</h1>
  <p>Lorem Ipsum is simply dummy text of the printing and typesetting industry. Lorem Ipsum has been the industry's standard dummy text ever since the 1500s, when an unknown printer took a galley of type and scrambled it to make a type specimen book. It has survived not only five centuries, but also the leap into electronic typesetting, remaining essentially unchanged. It was popularised in the 1960s with the release of Tessaline sheets containing Lorem Ipsum passages, and more recently with desktop publishing software like Pellmark Setter including versions of Lorem Ipsum.</p>
</section>
<a class="read-more" style="left:569px;top:699px">Read More</a>

<h2 class="products-title">Our Products</h2>

<div class="product" style="left:54px;top:771px"><div class="tint tone-fringe" role="img" aria-label="Green fringed trim on drapery fabric"></div><div class="more">more details<svg width="16" height="16" viewBox="0 0 16 16"><circle cx="8" cy="8" r="8" fill="#cfcfcf"/><path d="M6.5 4.5 10 8l-3.5 3.5" stroke="#fff" stroke-width="1.8" fill="none"/></svg></div></div>
<div class="product" style="left:245px;top:771px"><div class="tint tone-damask" role="img" aria-label="Beige damask cushion fabric"></div><div class="more">more details<svg width="16" height="16" viewBox="0 0 16 16"><circle cx="8" cy="8" r="8" fill="#cfcfcf"/><path d="M6.5 4.5 10 8l-3.5 3.5" stroke="#fff" stroke-width="1.8" fill="none"/></svg></div></div>
<div class="product" style="left:439px;top:771px"><div class="tint tone-ikat" role="img" aria-label="Blue and cream patterned textile"></div><div class="more">more details<svg width="16" height="16" viewBox="0 0 16 16"><circle cx="8" cy="8" r="8" fill="#cfcfcf"/><path d="M6.5 4.5 10 8l-3.5 3.5" stroke="#fff" stroke-width="1.8" fill="none"/></svg></div></div>
<div class="product" style="left:54px;top:940px"><div class="tint tone-fringe" role="img" aria-label="Green fringed trim on drapery fabric"></div><div class="more">more details<svg width="16" height="16" viewBox="0 0 16 16"><circle cx="8" cy="8" r="8" fill="#cfcfcf"/><path d="M6.5 4.5 10 8l-3.5 3.5" stroke="#fff" stroke-width="1.8" fill="none"/></svg></div></div>
<div class="product" style="left:245px;top:940px"><div class="tint tone-swatch" role="img" aria-label="Assorted fabric swatches in blue and rose"></div><div class="more">more details<svg width="16" height="16" viewBox="0 0 16 16"><circle cx="8" cy="8" r="8" fill="#cfcfcf"/><path d="M6.5 4.5 10 8l-3.5 3.5" stroke="#fff" stroke-width="1.8" fill="none"/></svg></div></div>
<div class="product" style="left:439px;top:940px"><div class="tint tone-fringe" role="img" aria-label="Green fringed trim on drapery fabric"></div><div class="more">more details<svg width="16" height="16" viewBox="0 0 16 16"><circle cx="8" cy="8" r="8" fill="#cfcfcf"/><path d="M6.5 4.5 10 8l-3.5 3.5" stroke="#fff" stroke-width="1.8" fill="none"/></svg></div></div>

<aside class="side-box testimonials">
  <h2>Testimonials</h2>
  <p class="quote">Lorem Ipsum is simply dummy text of the printing and typesetting industry. Lorem Ipsum has been the industry's standard</p>
  <p class="quote">Lorem Ipsum is simply dummy text of the printing and typesetting industry. Lorem Ipsum has been the industry's standard</p>
  <p class="quote">Lorem Ipsum is simply dummy text of the printing and typesetting industry. Lorem Ipsum has been the industry's standard</p>
  <a class="read-more" style="right:13px;bottom:6px">Read More</a>
</aside>

<aside class="side-box services">
  <h2>Services</h2>
  <ul class="service-list">
    <li>Lorem Ipsum is simply</li>
    <li>Lorem Ipsum is simply dummy</li>
    <li>Lorem Ipsum</li>
    <li>Lorem Ipsum is simply</li>
    <li>Lorem Ipsum is simply dummy</li>
  </ul>
  <a class="read-more" style="right:13px;bottom:18px">Read More</a>
</aside>

<footer class="site-footer">© 2012 - Terms of Service - Privacy Policy - Program Policies</footer>
</body>
</html>
```